Anzeigengestaltung für KURSHEFT WERK & GEFÜGE 2016/2017 –  BADEN-WÜRTTEMBERG
Anzeigengestaltung für KURSHEFT WERK & GEFÜGE 2016/2017 – BADEN-WÜRTTEMBERG
Zielgruppe
Wir sind ein mittelständischer Versicherungsmakler in Stuttgart und möchten eine halbe Seite in dem KURSHEFT WERK & GEFÜGE 2016/2017 – BADEN-WÜRTTEMBERG anbieten. Hier Informationen dazu:
'Jährlich drucken wir einen umfassenden Seminarkalender für unsere Mitglieds-unternehmen. Wir sind insgesamt vier Dienstleister der Weiterbildung für Verbands-mitgliedsbetriebe aus den Bereichen Hoch-, Straßen- und Tiefbau, Zimmerer- und Holzbau, Trockenbau, dem Stuckateurhandwerk und für Schreinerbetriebe.
 Lernwerkgesellschaft der Oberländischen Fachgewerke mbH
 Qualifizierungskreis der Rheintaler Handwerkerschaft GmbH
 Dienstkontor der Gewerkeverbände mbH Nordwald
 Hilfswerk-GmbH der Fachgewerke Kaiserstuhl
Als Partner unserer Betriebe möchten wir Ihnen diese Werbefläche für Ihre Kunden
anbieten. Das Seminarprogramm ist bei unseren Betrieben seit Jahren eingeführt und ein
wichtiges Druckwerk. Das geplante Programm 2016/2017 umfasst ca. 200 Seminare
im Zeitraum September 2016 bis Juli 2017.
Der Seminarkalender wird all unseren Mitgliedsbetrieben, insgesamt 2.500 Betriebe,
im August/September 2016 per Post zugesandt. Das Verteilungsgebiet erstreckt sich
über Württemberg und Südbaden. In diesem Jahr, aufgrund einer gestiegenen Nachfrage
über das Verteilungsgebiet hinaus, in einer erhöhten Auflage von ca. 6.000 Stück.
Die Unternehmen nutzen die Broschüre über ein Jahr zur Planung ihrer Weiterbildung.
Diese attraktive Werbeplattform bieten wir Ihnen an! Gerne nehmen wir Ihre Werbung
mit in das Programm auf.'
Wir wollen durch die Anzeige neue Kunden werben speziell in der o. g. Branche (Bau), da wir darauf spezialisiert sind.
Aufgabenstellung
Anzeige soll modern sein, einladend. Es soll rüberkommen, dass wir der perfekte Versicherungsmakler für die Branche sind und innovative und spezielle Lösungen anbieten können.
Da hier ein Versicherer (die PLR) sehr auffällig und groß wirbt (mit Gelb und schwarz) sollte unsere Anzeige schon auch auffallen.
Unsere Kontaktdaten sollen erscheinen und eventuell ein Ansprechpartner (dies je nach Empfehlung Ihrerseits).
Puristisch aber auffallend. Interessant und Neugierig soll die Anzeige sein. Unser Leitspruch: Zuverlässig. Kompetent. Vertrauensvoll. Wir sind Ihr Partner!
Unsere Farben:
Dunkler Blauton in RGB: 48 / 72 / 162, der helle Blauton in RGB: 44 / 152 / 224
Hier die Informationen zur Anzeige die uns vorliegen:
Anzeigenformat:
Breite 210 mm x Höhe 140mm (Beschnitt rechts und links ohne Schnittmarken)
Datenformat: Breite 216 x Höhe 140 mm
Nur digitale Vorlagen einsenden.
1. Anzeigen, druckfähige / reprofähige PDF-Daten
Schriften und Bilddaten vollständig eingebettet, "PDF-X3-Standard"
Generell keine Schnittmarken o. ä.
2. Produktabbildung, druckfähige/ reprofähige Daten, TIF- oder JPG-Bilddaten
Halbtonbilder mindestens 300 dpi, Strichbilder 1200 dpi
Frist zur Einsendung ist der 06.05.2016!

```html
<!DOCTYPE html>
<html lang="de">
<head>
<meta charset="utf-8">
<title>Anzeige Nordlicht Risikoberatung – Kursheft Werk &amp; Gefüge</title>
<link rel="stylesheet" href="https://fonts.googleapis.com/css2?family=Source+Sans+3:ital,wght@0,400;0,600;0,700;1,700&display=swap">
<style>
  :root {
    --blue-dark: rgb(48, 72, 162);
    --blue-light: rgb(44, 152, 224);
    --red: #c8202a;
    --white: #ffffff;
    --stage: #dcdcdc;
    --wall-1: #f1ede6;
    --wall-2: #d9d3c9;
  }
  * { margin: 0; padding: 0; box-sizing: border-box; }
  html, body {
    width: 1200px; height: 1200px; overflow: hidden;
    background: var(--stage);
    font-family: "Source Sans 3", "Myriad Pro", Arial, sans-serif;
  }
  .ad {
    position: absolute; left: 48px; top: 233px;
    width: 1104px; height: 734px;
    background: var(--white);
    overflow: hidden;
  }
  .contact-panel {
    position: absolute; left: 0; top: 194px;
    width: 451px; height: 331px;
    background: var(--blue-light);
  }
  .brand {
    position: absolute; left: 52px; top: 60px;
    display: flex; align-items: center; gap: 24px;
  }
  .brand-mark {
    width: 72px; height: 72px; background: var(--blue-light);
  }
  .brand-name {
    font-size: 20px; font-weight: 400; line-height: 1.2;
    color: var(--blue-dark);
  }
  .call-box {
    position: absolute; left: 112px; top: 180px;
    width: 313px; height: 92px;
    background: var(--red);
    transform: rotate(-3deg);
    box-shadow: 0 3px 6px rgba(0,0,0,.25);
    color: var(--white);
    text-align: center;
    padding-top: 10px;
  }
  .call-box .call-text {
    font-size: 17px; font-weight: 700; line-height: 1.2;
  }
  .call-box .call-number {
    margin-top: 4px;
    font-size: 27px; font-weight: 700;
    display: flex; align-items: center; justify-content: center; gap: 8px;
  }
  .address {
    position: absolute; left: 52px; top: 338px;
    color: var(--white);
    font-size: 19px; line-height: 28px;
    font-style: normal;
  }
  .photo {
    position: absolute; left: 451px; top: 0;
    width: 653px; height: 525px;
    background: linear-gradient(135deg, var(--wall-1) 0%, var(--wall-2) 100%);
  }
  .headline {
    position: absolute; left: 480px; top: 44px;
    font-weight: 700; line-height: 1;
    text-transform: uppercase;
  }
  .headline span { display: block; }
  .headline .h-innovative { font-size: 44px; color: var(--blue-dark); }
  .headline .h-loesungen { font-size: 64px; color: var(--blue-light); margin-left: 28px; margin-top: -2px; }
  .headline .h-fuer { font-size: 46px; color: var(--blue-dark); margin-left: 52px; margin-top: -4px; }
  .headline .h-bau { font-size: 66px; color: var(--blue-light); margin-top: -4px; }
  .claim-band {
    position: absolute; left: 0; top: 525px;
    width: 1052px; height: 84px;
    background: var(--blue-dark);
    color: var(--white);
    font-size: 56px; font-weight: 700; font-style: italic;
    display: flex; align-items: center;
    padding-left: 56px;
    white-space: nowrap;
  }
  .motto {
    position: absolute; left: 451px; top: 609px;
    width: 601px; height: 49px;
    background: var(--blue-light);
    color: var(--white);
    font-size: 26px; font-weight: 400; letter-spacing: 0.5px;
    display: flex; align-items: center; justify-content: center;
    white-space: nowrap;
  }
</style>
</head>
<body>
  <main class="ad">
    <div class="photo" role="img" aria-label="Foto: junger Bauarbeiter mit gelbem Helm, blauer Arbeitskleidung und Vorschlaghammer vor heller Backsteinwand, Daumen hoch"></div>

    <div class="brand">
      <div class="brand-mark"></div>
      <div class="brand-name">Nordlicht Risikoberatung<br>Aktiengesellschaft</div>
    </div>

    <div class="contact-panel"></div>

    <div class="call-box">
      <p class="call-text">Rufen Sie uns an und vereinbaren<br>einen unverbindlichen Termin</p>
      <p class="call-number">
        <svg width="20" height="20" viewBox="0 0 24 24" aria-hidden="true">
          <circle cx="12" cy="12" r="11" fill="none" stroke="#fff" stroke-width="2"/>
          <path d="M8.5 6.5c-.8.3-1.5 1.2-1.4 2.3.3 3.5 4.6 8 8.2 8.3 1.1.1 2-.6 2.3-1.4l-2.2-1.6-1.3 1c-1.6-.6-3.5-2.5-4.1-4.1l1-1.3z" fill="#fff"/>
        </svg>
        0711 480 22 - 0
      </p>
    </div>

    <address class="address">
      Lindenhofweg 7<br>
      70569 Stuttgart<br>
      Telefon: 0711 480 22 - 0<br>
      Telefax: 0711 480 22 - 30<br>
      www.nordlicht-beratung-beispiel.de<br>
      kontakt@nordlicht-beratung-beispiel.de
    </address>

    <h1 class="headline">
      <span class="h-innovative">Innovative</span>
      <span class="h-loesungen">Lösungen</span>
      <span class="h-fuer">für die</span>
      <span class="h-bau">Baubranche</span>
    </h1>

    <p class="claim-band">Ihr Partner in allen Versicherungsfragen</p>
    <p class="motto">ZUVERLÄSSIG. KOMPETENT. VERTRAUENSVOLL.</p>
  </main>
</body>
</html>
```